Online medical reviews website needs banner advert!

We need banner advert templates for our website, www.traineepanel.net. These should meet the technical requirements of our partner (uploaded).

Our groundbreaking website allows doctors in training to rate and review their training.

The adverts should use the same modern design language and colour scheme as our website. They should use the text 'Help a junior doctor make a big decision - rate your training!'.

Vector assets should be supplied, allowing us to use alternative text in future.
Updates

Industry/Entity Type

Healthcare

Font styles to use
Other font styles liked:
• Karla

Colors
3277b5
0555a3
ffffff

Requirements
Must have
• Similar design to our website. Should be elegant & modern. Must allow future text to be easily inserted.
Should not have
• Unrelated design.

```html
<!DOCTYPE html>
<html lang="en">
<head>
<meta charset="UTF-8">
<title>Rate your training banner</title>
<link rel="stylesheet" href="https://fonts.googleapis.com/css2?family=Karla:wght@800&display=swap">
<style>
  :root {
    --brand-blue: #3277b5;
    --brand-navy: #0555a3;
    --deep-blue: #1a3fcf;
    --glow-cyan: #bff8f2;
    --mid-teal: #4fb6cc;
    --shade-navy: rgba(14, 48, 120, 0.55);
    --ink-outline: #0b2a6e;
    --white: #ffffff;
  }
  html, body {
    margin: 0;
    padding: 0;
    overflow: hidden;
    background: var(--white);
  }
  .banner {
    position: relative;
    width: 1200px;
    height: 589px;
    overflow: hidden;
    font-family: "Karla", Arial, sans-serif;
  }
  .banner__backdrop {
    position: absolute;
    inset: 0;
    background:
      radial-gradient(ellipse 30% 45% at 48% 48%, rgba(191, 248, 242, 0.9) 0%, rgba(120, 215, 225, 0.6) 40%, rgba(79, 182, 204, 0) 80%),
      radial-gradient(ellipse 75% 85% at 52% 50%, var(--mid-teal) 0%, var(--brand-blue) 55%, var(--deep-blue) 100%);
  }
  .banner__helix {
    position: absolute;
    left: 0;
    top: 0;
    width: 470px;
    height: 589px;
    background:
      radial-gradient(ellipse 18% 22% at 72% 45%, rgba(150, 240, 240, 0.55) 0%, rgba(150, 240, 240, 0) 100%),
      linear-gradient(90deg, rgba(26, 63, 207, 0.85) 0%, rgba(30, 80, 180, 0.45) 45%, rgba(50, 119, 181, 0) 100%);
  }
  .banner__molecules {
    position: absolute;
    border-radius: 50%;
    background: radial-gradient(closest-side, var(--shade-navy) 0%, rgba(14, 48, 120, 0.25) 55%, rgba(14, 48, 120, 0) 100%);
  }
  .banner__molecules--top { left: 590px; top: -30px; width: 250px; height: 150px; }
  .banner__molecules--right { left: 950px; top: 420px; width: 260px; height: 190px; }
  .banner__molecules--small-right { left: 975px; top: 165px; width: 50px; height: 50px; }
  .banner__molecules--small-centre { left: 752px; top: 415px; width: 50px; height: 50px; }
  .banner__headline {
    position: absolute;
    left: 0;
    right: 0;
    top: 266px;
    margin: 0;
    text-align: center;
    font-size: 38px;
    font-weight: 800;
    letter-spacing: 0.2px;
    color: var(--white);
    -webkit-text-stroke: 1.2px var(--ink-outline);
    text-shadow:
      0 0 2px var(--ink-outline),
      0 0 5px rgba(255, 255, 255, 0.95),
      0 0 9px rgba(255, 255, 255, 0.6);
    white-space: nowrap;
  }
</style>
</head>
<body>
  <main class="banner">
    <div class="banner__backdrop" role="img" aria-label="Glowing cyan and blue science backdrop with a faint square grid"></div>
    <div class="banner__helix" role="img" aria-label="DNA double helix rising along the left side"></div>
    <div class="banner__molecules banner__molecules--top" role="img" aria-label="Dark molecule models at the top centre"></div>
    <div class="banner__molecules banner__molecules--small-right" role="img" aria-label="Small molecule model"></div>
    <div class="banner__molecules banner__molecules--small-centre" role="img" aria-label="Small molecule model"></div>
    <div class="banner__molecules banner__molecules--right" role="img" aria-label="Dark molecule models at the lower right"></div>
    <h1 class="banner__headline">Help a junior doctor make a big decision - rate your training !</h1>
  </main>
</body>
</html>
```